Welding company needs a business card

We are looking for a logo and business card.

Contact Information for Business Card

418 Bramblecrest Lane
Salem, OR 97301
503-555-0173
Kvmetalcraft@forgepostbox.net

```html
<!DOCTYPE html>
<html lang="en">
<head>
<meta charset="utf-8">
<title>Ridgeline Forge Co — Business Card</title>
<link rel="stylesheet" href="https://fonts.googleapis.com/css2?family=Jost:wght@400;500;700&display=swap">
<style>
  :root {
    --page-bg: #ececec;
    --card-dark: #333335;
    --card-light: #fafafa;
    --ink-dark: #2b2b2d;
    --ink-muted: #6a6a6a;
    --ink-light: #ffffff;
    --flame-red: #e8372f;
    --flame-orange: #f27a2a;
    --flame-yellow: #fdc113;
  }
  * { box-sizing: border-box; margin: 0; padding: 0; }
  html, body {
    width: 1200px; height: 800px; overflow: hidden;
    background: var(--page-bg);
    font-family: "Jost", "Futura", sans-serif;
  }
  .sheet {
    position: relative; width: 1200px; height: 800px;
    display: flex; align-items: center; justify-content: center; gap: 60px;
  }
  .card {
    position: relative; width: 520px; height: 297px; overflow: hidden;
    box-shadow: 0 10px 24px rgba(0,0,0,0.14);
  }
  .card--front { background: var(--card-dark); }
  .card--back { background: var(--card-light); }
  .card__band { position: absolute; inset: 0; width: 100%; height: 100%; }

  .brand { position: absolute; }
  .brand__mark {
    position: absolute; width: 56px; height: 56px; border-radius: 50%;
  }
  .brand__name {
    font-weight: 700; font-size: 29px; letter-spacing: 0.5px; line-height: 1;
    padding-bottom: 8px; border-bottom: 1.5px solid currentColor; white-space: nowrap;
  }
  .brand__tagline {
    font-weight: 400; font-size: 16px; letter-spacing: 0.8px; margin-top: 7px;
    white-space: nowrap;
  }

  .card--front .brand { left: 40px; top: 100px; color: var(--ink-light); }
  .card--front .brand__mark { background: var(--ink-light); right: 4px; top: -66px; }

  .card--back .brand { left: 176px; top: 90px; color: var(--ink-dark); }
  .card--back .brand__mark { background: var(--ink-dark); right: 0; top: -66px; }
  .card--back .brand__tagline { color: var(--ink-muted); }

  .contact {
    position: absolute; display: flex; align-items: center; gap: 10px;
    font-size: 15px; font-weight: 500; color: var(--ink-dark); white-space: nowrap;
  }
  .contact svg { flex: none; }
  .contact--phone { left: 34px; top: 58px; }
  .contact--email { left: 200px; top: 172px; }
  .contact--address {
    left: 0; right: 0; justify-content: center; top: 242px;
    color: var(--ink-light); font-size: 16px; letter-spacing: 0.4px;
  }
</style>
</head>
<body>
<main class="sheet">

  <section class="card card--front" aria-label="Card front">
    <svg class="card__band" viewBox="0 0 520 297" preserveAspectRatio="none" aria-hidden="true">
      <defs>
        <linearGradient id="front-flame" x1="0" y1="0" x2="1" y2="1">
          <stop offset="0" stop-color="var(--flame-red)"/>
          <stop offset="0.45" stop-color="var(--flame-orange)"/>
          <stop offset="1" stop-color="var(--flame-yellow)"/>
        </linearGradient>
      </defs>
      <polygon points="0,205 390,262 520,262 520,297 0,297" fill="url(#front-flame)"/>
    </svg>
    <div class="brand">
      <span class="brand__mark"></span>
      <p class="brand__name">RIDGELINE FORGE CO</p>
      <p class="brand__tagline">Mobile Welding &amp; Fabrication</p>
    </div>
  </section>

  <section class="card card--back" aria-label="Card back">
    <svg class="card__band" viewBox="0 0 520 297" preserveAspectRatio="none" aria-hidden="true">
      <defs>
        <linearGradient id="back-flame" x1="0" y1="0" x2="1" y2="0.4">
          <stop offset="0" stop-color="var(--flame-red)"/>
          <stop offset="0.5" stop-color="var(--flame-orange)"/>
          <stop offset="1" stop-color="var(--flame-yellow)"/>
        </linearGradient>
      </defs>
      <polygon points="0,25 70,222 445,222 472,204 520,204 520,297 0,297" fill="url(#back-flame)"/>
    </svg>

    <div class="brand">
      <span class="brand__mark"></span>
      <p class="brand__name">RIDGELINE FORGE CO</p>
      <p class="brand__tagline">Mobile Welding &amp; Fabrication</p>
    </div>

    <p class="contact contact--phone">
      <svg width="14" height="20" viewBox="0 0 14 20" aria-hidden="true">
        <rect x="1" y="1" width="12" height="18" rx="2" fill="none" stroke="var(--flame-orange)" stroke-width="1.5"/>
        <line x1="5" y1="16" x2="9" y2="16" stroke="var(--flame-orange)" stroke-width="1.5"/>
      </svg>
      503-555-0173
    </p>

    <p class="contact contact--email">
      <svg width="22" height="16" viewBox="0 0 22 16" aria-hidden="true">
        <rect x="1" y="1" width="20" height="14" fill="none" stroke="var(--flame-orange)" stroke-width="1.5"/>
        <polyline points="1,1 11,9 21,1" fill="none" stroke="var(--flame-orange)" stroke-width="1.5"/>
      </svg>
      Kvmetalcraft@forgepostbox.net
    </p>

    <p class="contact contact--address">418 Bramblecrest Lane, Salem, OR 97301</p>
  </section>

</main>
</body>
</html>
```